Letterhead Design Project

I need a simple, clean and corporate letterhead & follow-on letterhead.
The follow-on letterhead should just have the logo only.
Final File Specs:
Full Bleed Size (starting document size)
213 x 300 mm
2517 x 3544 pixels
* Finished artwork should use the full bleed dimensions for best results.
Document Trim Size (final size after being cut)
210 x 297 mm
2480 x 3508 pixels
* Please be sure to keep all text within the safe margin.
Resolution 300 DPI
Accepted file types:-
Adobe Acrobat 9 Document (*.pdf) (recommended)
Adobe Illustrator CS3 Artwork (*.ai) (recommended)
Adobe Photoshop CS3 Image (*.psd) (recommended)
Bitmap Image (*.bmp)
GIF Image (*.gif)
JPEG Image (*.jpg,*.jpeg)
Microsoft PowerPoint 2010 Document (*.ppt)
Microsoft Publisher 2010 Document (*.pub)
Microsoft Word 2010 Document (*.doc)
PCX Image (*.pcx)
PICT Image (*.pic,*.pict,*.pct)
PNG Image (*.png)
PostScript Document (*.ps)
TIF Image (*.tif,*.tiff)
Windows Enhanced Metafile (*.emf)
Windows Metafile (*.wmf)
Requirements
Must have
- My letterhead must have:-
- Logo
- ACN - 418 572 906
- address - Suite 8, 19 Heron St, Maroubra, NSW 2035
- phone - (02) 9361 4258
- fax - (02) 9517 3046
- email - info@brimtarsafety.com.au
- web - www.brimtarsafety.com.au
Follow-on letterhead should have the logo only

```html
<!DOCTYPE html>
<html lang="en">
<head>
<meta charset="utf-8">
<title>Brimtar Asbestos &amp; Safety — Letterhead</title>
<link rel="stylesheet" href="https://fonts.googleapis.com/css2?family=Questrial&family=Mulish:wght@700&display=swap">
<style>
  :root {
    --backdrop: #e9edee;
    --paper: #ffffff;
    --navy: #221c44;
    --lime: #9bd31d;
    --shadow: rgba(20, 40, 45, 0.25);
  }
  * { margin: 0; padding: 0; box-sizing: border-box; }
  html, body {
    width: 1200px;
    height: 900px;
    overflow: hidden;
    background: var(--backdrop);
  }
  .letterhead {
    position: absolute;
    left: 317px;
    top: 50px;
    width: 566px;
    height: 800px;
    background: var(--lime);
    box-shadow: 0 6px 22px var(--shadow);
    font-family: "Questrial", "Century Gothic", sans-serif;
    color: var(--navy);
  }
  .letterhead__sheet {
    position: absolute;
    inset: 0 0 26px 0;
    background: var(--paper);
    border-radius: 0 0 14px 14px;
  }
  .brand {
    position: absolute;
    top: 44px;
    right: 34px;
    display: flex;
    align-items: center;
    gap: 8px;
  }
  .brand__mark {
    width: 20px;
    height: 20px;
    background: var(--lime);
  }
  .brand__name {
    font-size: 19px;
    line-height: 1;
    color: var(--navy);
    letter-spacing: 0.2px;
  }
  .contact {
    position: absolute;
    left: 0;
    right: 0;
    bottom: 14px;
    text-align: center;
    line-height: 1.55;
  }
  .contact__acn { font-size: 9.5px; }
  .contact__address {
    font-family: "Mulish", "Century Gothic", sans-serif;
    font-weight: 700;
    font-size: 9.5px;
  }
  .contact__lines {
    display: flex;
    justify-content: center;
    gap: 12px;
    font-size: 9.5px;
    list-style: none;
  }
  .contact__lines li {
    display: flex;
    align-items: center;
    gap: 4px;
  }
  .contact__icon { width: 9px; height: 9px; fill: var(--navy); }
</style>
</head>
<body>
  <main class="letterhead">
    <div class="letterhead__sheet">
      <header class="brand">
        <span class="brand__mark"></span>
        <span class="brand__name">Brimtar Asbestos &amp; Safety</span>
      </header>

      <footer class="contact">
        <p class="contact__acn">ACN - 418 572 906</p>
        <p class="contact__address">Suite 8, 19 Heron St, Maroubra, NSW 2035</p>
        <ul class="contact__lines">
          <li>
            <svg class="contact__icon" viewBox="0 0 10 10" aria-hidden="true"><rect x="2.5" y="0.5" width="5" height="9" rx="1"/><rect x="3.5" y="1.8" width="3" height="5" fill="#fff"/></svg>
            (02) 9361 4258
          </li>
          <li>
            <svg class="contact__icon" viewBox="0 0 10 10" aria-hidden="true"><rect x="2.5" y="0.5" width="5" height="3"/><rect x="0.5" y="3.5" width="9" height="4.5" rx="1"/><rect x="2.5" y="7" width="5" height="2.5" fill="#fff" stroke="#221c44" stroke-width="0.8"/></svg>
            (02) 9517 3046
          </li>
          <li>
            <svg class="contact__icon" viewBox="0 0 10 10" aria-hidden="true"><rect x="0.5" y="2" width="9" height="6.5" rx="0.6"/><path d="M1 2.6 L5 5.6 L9 2.6" fill="none" stroke="#fff" stroke-width="0.9"/></svg>
            info@brimtarsafety.com.au
          </li>
          <li>
            <svg class="contact__icon" viewBox="0 0 10 10" aria-hidden="true"><circle cx="5" cy="5" r="4.5"/><path d="M0.8 5 H9.2 M5 0.6 V9.4 M5 0.6 C2.5 3 2.5 7 5 9.4 M5 0.6 C7.5 3 7.5 7 5 9.4" fill="none" stroke="#fff" stroke-width="0.7"/></svg>
            www.brimtarsafety.com.au
          </li>
        </ul>
      </footer>
    </div>
  </main>
</body>
</html>
```